Dennis K. Halvorsen stationery and new logo

Create Word template stationery, with a logo, for a Forensic Psychiatry business.

The stationery must include contact info (see below)

The logo should include images similar to (but not necessarily identical to) the ones in the uploaded document. They are the scales of justice and the caduceus, or staff, associated with medicine.

Target Market(s)

consumers of forensic psychiatry (usually lawyers and their clients)

Industry/Entity Type

Mental Health

Logo Text

Dennis K. Halvorsen, MD, DLFAPA

Font styles to use
Serif

Colors

Designer to choose colors to be used in the design.

Requirements
Must have
• Forensic Psychiatry
• 715 N. Maple Street
• R Building
• West Ashford, PA 19804
• (484) 555-3172
Nice to have
• Conservative color scheme

```html
<!DOCTYPE html>
<html lang="en">
<head>
<meta charset="utf-8">
<title>Dennis K. Halvorsen — Stationery</title>
<link rel="stylesheet" href="https://fonts.googleapis.com/css2?family=Cinzel:wght@500&family=Lato:wght@400&display=swap">
<style>
  :root {
    --backdrop: #d4d5d7;
    --brand-blue: #3773a0;
    --brand-green: #84b942;
    --paper: #ffffff;
    --ink: #6a6a6a;
    --ink-soft: #8a8a8a;
  }
  * { margin: 0; padding: 0; box-sizing: border-box; }
  html, body { width: 1200px; height: 1191px; overflow: hidden; }
  body {
    position: relative;
    background: var(--backdrop);
    font-family: "Lato", Arial, sans-serif;
    color: var(--ink);
  }
  .abs { position: absolute; }
  .serif { font-family: "Cinzel", "Times New Roman", serif; font-weight: 500; }

  /* Folder */
  .folder-flaps { left: 0; top: 0; width: 1200px; height: 1191px; }
  .folder-cover { left: 166px; top: 65px; width: 371px; height: 511px; background: var(--brand-blue); }
  .folder-front { left: 537px; top: 65px; width: 372px; height: 511px; background: var(--paper); }
  .folder-contact { left: 49px; top: 424px; color: #fff; font-size: 7.6px; line-height: 13px; }
  .folder-contact .row { display: flex; align-items: flex-start; gap: 7px; }
  .folder-contact .row + .row { margin-top: 3px; }
  .folder-wordmark { left: 126px; top: 225px; color: var(--brand-blue); }

  .wordmark .name { display: block; font-size: 17px; line-height: 1; letter-spacing: 0.3px; }
  .wordmark .cred { display: block; font-size: 11px; line-height: 1; margin-top: 5px; }

  .icon { width: 8px; height: 8px; flex: none; margin-top: 2px; }
  .icon-white { fill: #fff; }
  .icon-green { fill: var(--brand-green); }

  /* Business cards */
  .card-front { left: 870px; top: 186px; width: 202px; height: 115px; background: var(--brand-blue); }
  .card-front .wordmark { position: absolute; left: 74px; top: 49px; color: #fff; }
  .card-front .name { font-size: 8px; }
  .card-front .cred { font-size: 5px; margin-top: 2px; }

  .card-back { left: 871px; top: 319px; width: 202px; height: 115px; background: var(--paper); }
  .card-back .holder { position: absolute; left: 20px; top: 22px; }
  .card-back .holder-name { font-size: 7px; color: var(--brand-blue); line-height: 1; }
  .card-back .holder-role { font-size: 4.6px; color: var(--brand-green); line-height: 1; margin-top: 1px; }
  .card-back .contact { position: absolute; left: 20px; top: 68px; font-size: 4.4px; line-height: 6px; color: var(--ink); }
  .card-back .row { display: flex; gap: 4px; }
  .card-back .row + .row { margin-top: 4px; }
  .card-back .icon { width: 4.5px; height: 4.5px; margin-top: 1px; }

  /* Envelope */
  .envelope-flap { left: 152px; top: 771px; width: 499px; height: 83px; }
  .envelope { left: 152px; top: 853px; width: 499px; height: 250px; background: var(--paper); }
  .envelope .wordmark { position: absolute; left: 85px; top: 47px; color: var(--brand-blue); }
  .envelope .name { font-size: 13.5px; }
  .envelope .cred { font-size: 8.5px; margin-top: 4px; }
  .envelope .contact { position: absolute; left: 42px; top: 152px; font-size: 9.5px; line-height: 15px; color: var(--ink); }
  .envelope .row { display: flex; gap: 6px; }
  .envelope .icon { width: 8px; height: 8px; margin-top: 3px; }
  .envelope-window {
    position: absolute; left: 293px; top: 119px; width: 166px; height: 73px; border-radius: 3px;
    background: linear-gradient(120deg, #76a33c 0%, #8fc04f 45%, #a2cd6c 50%, #8ebf4e 70%, #72a038 100%);
    box-shadow: -4px 3px 0 #cfd0d2;
  }

  /* Letterhead */
  .letterhead { left: 692px; top: 628px; width: 360px; height: 509px; background: var(--paper); }
  .letterhead .wordmark { position: absolute; left: 52px; top: 59px; color: var(--brand-blue); }
  .letterhead .name { font-size: 8px; }
  .letterhead .cred { font-size: 5px; margin-top: 2px; }
  .letterhead .contact { position: absolute; left: 246px; top: 57px; font-size: 4.5px; line-height: 6px; }
  .letterhead .contact .row { display: flex; gap: 4px; }
  .letterhead .contact .row + .row { margin-top: 4px; }
  .letterhead .contact .icon { width: 4.5px; height: 4.5px; margin-top: 0.5px; }
  .letter-body { position: absolute; left: 24px; top: 162px; width: 314px; font-size: 5.4px; line-height: 9.6px; color: var(--ink); }
  .letter-meta { display: flex; justify-content: space-between; margin-bottom: 15px; }
  .letter-body p { text-align: justify; margin-bottom: 9px; }
  .sign-off { position: absolute; left: 24px; top: 315px; color: #4a4a4a; }
  .sign-off .signer { font-size: 8.5px; line-height: 1; }
  .sign-off .signer-role { font-size: 5.6px; color: var(--ink-soft); margin-top: 1px; }
  .signature {
    margin-top: 6px; width: 82px; height: 30px;
    background: linear-gradient(100deg, rgba(40,60,140,0.05), rgba(40,60,140,0.14), rgba(40,60,140,0.05));
    border-bottom: 0.6px solid #c7c9d6;
  }
</style>
</head>
<body>

<svg width="0" height="0" style="position:absolute" aria-hidden="true">
  <defs>
    <symbol id="icon-phone" viewBox="0 0 24 24">
      <path d="M6.6 10.8a15.1 15.1 0 0 0 6.6 6.6l2.2-2.2c.3-.3.7-.4 1-.2 1.1.4 2.3.6 3.6.6.6 0 1 .4 1 1V20c0 .6-.4 1-1 1A17 17 0 0 1 3 4c0-.6.4-1 1-1h3.5c.6 0 1 .4 1 1 0 1.3.2 2.5.6 3.6.1.3 0 .7-.2 1z"/>
    </symbol>
    <symbol id="icon-pin" viewBox="0 0 24 24">
      <path d="M12 2a7 7 0 0 0-7 7c0 5.2 7 13 7 13s7-7.8 7-13a7 7 0 0 0-7-7zm0 9.5A2.5 2.5 0 1 1 12 6.5a2.5 2.5 0 0 1 0 5z"/>
    </symbol>
  </defs>
</svg>

<!-- Folder -->
<svg class="abs folder-flaps" viewBox="0 0 1200 1191" aria-hidden="true">
  <polygon points="94,107 166,65 166,576 94,525" fill="var(--brand-green)"/>
  <polygon points="166,576 537,576 475,661 166,661" fill="var(--brand-green)"/>
</svg>

<section class="abs folder-cover">
  <div class="abs folder-contact">
    <div class="row"><svg class="icon icon-white"><use href="#icon-phone"/></svg><span>Phone : (484) 555-3172</span></div>
    <div class="row"><svg class="icon icon-white"><use href="#icon-pin"/></svg><span>Location : 715 N. Maple Street<br>R Building West Ashford, PA 19804</span></div>
  </div>
</section>

<section class="abs folder-front">
  <div class="abs wordmark folder-wordmark serif">
    <span class="name">Dennis K. Halvorsen</span>
    <span class="cred">MD, DLFAPA</span>
  </div>
</section>

<!-- Business cards -->
<section class="abs card-front">
  <div class="wordmark serif">
    <span class="name">Dennis K. Halvorsen</span>
    <span class="cred">MD, DLFAPA</span>
  </div>
</section>

<section class="abs card-back">
  <div class="holder serif">
    <div class="holder-name">YOUR NAME</div>
    <div class="holder-role">Designation</div>
  </div>
  <div class="contact">
    <div class="row"><svg class="icon icon-green"><use href="#icon-phone"/></svg><span>Phone : (484) 555-3172</span></div>
    <div class="row"><svg class="icon icon-green"><use href="#icon-pin"/></svg><span>Location : 715 N. Maple Street<br>R Building West Ashford, PA 19804</span></div>
  </div>
</section>

<!-- Envelope -->
<svg class="abs envelope-flap" viewBox="0 0 499 83" aria-hidden="true">
  <path d="M0,83 L9,8 Q10,0 20,0 L480,1 Q488,1 490,9 L499,83 Z" fill="var(--brand-green)"/>
</svg>

<section class="abs envelope">
  <div class="wordmark serif">
    <span class="name">Dennis K. Halvorsen</span>
    <span class="cred">MD, DLFAPA</span>
  </div>
  <div class="contact">
    <div class="row"><svg class="icon icon-green"><use href="#icon-phone"/></svg><span>Phone : (484) 555-3172</span></div>
    <div class="row"><svg class="icon icon-green"><use href="#icon-pin"/></svg><span>Location : 715 N. Maple Street<br>R Building West Ashford, PA 19804</span></div>
  </div>
  <div class="envelope-window"></div>
</section>

<!-- Letterhead -->
<section class="abs letterhead">
  <div class="wordmark serif">
    <span class="name">Dennis K. Halvorsen</span>
    <span class="cred">MD, DLFAPA</span>
  </div>
  <div class="contact">
    <div class="row"><svg class="icon icon-green"><use href="#icon-phone"/></svg><span>Phone : (484) 555-3172</span></div>
    <div class="row"><svg class="icon icon-green"><use href="#icon-pin"/></svg><span>Location : 715 N. Maple Street<br>R Building West Ashford, PA 19804</span></div>
  </div>

  <div class="letter-body">
    <div class="letter-meta"><span>Dear, Mr___________</span><span>Date : 4.01.2020</span></div>
    <p>Lorem Ipsum is simply dummy text of the printing and typesetting industry. Lorem Ipsum has been the industry's standard dummy text ever since the1500s,when an unknown printer took a galley of type and scrambled it to make a type specimen book. It has survived not only five centuries, but also the leap into electronic typesetting, remaining essentially unchanged.</p>
    <p>Lorem Ipsum is simply dummy text of the printing and typesetting industry. Lorem Ipsum has been the industry's standard dummy text ever since the1500s.</p>
    <p>Lorem Ipsum is simply dummy text of the printing and typesetting industry.</p>
  </div>

  <div class="sign-off">
    <div class="signer">Your Name</div>
    <div class="signer-role">Designation</div>
    <div class="signature" role="img" aria-label="Handwritten signature"></div>
  </div>
</section>

</body>
</html>
```